Monthly Mailed Newsletter/Magazine for Medical Spa

Every month we send out a mailed newsletter/magazine to our visitors from the previous month. We made a sample newsletter/magazine as a guideline of what we are looking for. We need a designer to make a simple and clean design layout.

- Attached is our sample design that has all the content we want to use.
- Newsletter/magazine is 8 pages total.
- Size of each page is 8.5 inches in width by 11 inches in height.
- Content and images can be located here: https://files.quorvadrop.net/share/folders/8kTrmWq2Zp7ncV4Lx91aHd0sYuE3Gb6Rj?access=open

The following will give you an idea of our brand presentation.
Our website is: www.FernBloomClinic.com
Our Instagram; @fernbloomclinic
Our Facebook: www.friendvault.com/fernbloomclinic

Target Market(s)

Women 25 - 45

Industry/Entity Type

Beauty

Other font styles liked:
• Josefins Sans Bold & Lato

Colors
f78f20
ffffff

Requirements
Must have
• - Our Logo
- Our tagline: YOUR SKIN DESERVES IT!
- Address and contact information for our locations
- Our color scheme: Black and #FAA641
- Heading font is Josefin Sans Bold
- Paragraph font is Lato
- Our website address: www.FernBloomClinic.com

```html
<!DOCTYPE html>
<html lang="en">
<head>
<meta charset="utf-8">
<title>Can You Make Your Neurelax Last Longer? – FernBloom Clinic</title>
<link rel="stylesheet" href="https://fonts.googleapis.com/css2?family=Archivo:wght@800&family=Roboto:wght@400;700&display=swap">
<style>
  :root {
    --page-bg: #ffffff;
    --brand-orange: #eba640;
    --accent-red: #e8541e;
    --headline-light: #f6f2ec;
    --heading-orange: #eb9e38;
    --body-ink: #2a2a2a;
    --brand-ink: #1d1d1d;
    --rule: #f3d69c;
    --photo-light: #e9e4df;
    --photo-mid: #b98866;
  }
  * { margin: 0; padding: 0; box-sizing: border-box; }
  html, body {
    width: 1200px; height: 1000px; overflow: hidden;
    background: var(--page-bg);
  }
  .canvas { position: relative; width: 1200px; height: 1000px; }
  .page-art { position: absolute; left: 0; top: 0; }
  .headline {
    position: absolute; left: 270px; top: 82px;
    font-family: "Archivo", "Arial Black", sans-serif;
    font-weight: 800;
    font-size: 36px; line-height: 44.5px;
    color: var(--headline-light);
    text-transform: uppercase; letter-spacing: 0;
  }
  .article {
    position: absolute; left: 270px;
    font-family: "Roboto", Arial, sans-serif;
    font-size: 12.3px; line-height: 21.5px;
    color: var(--body-ink);
  }
  .intro { top: 536px; white-space: nowrap; }
  .section-heading {
    position: absolute; left: 270px;
    font-family: "Archivo", "Arial Black", sans-serif;
    font-weight: 800;
    font-size: 21px; line-height: 26px;
    color: var(--heading-orange);
  }
  .heading-how { top: 642px; }
  .heading-last { top: 760px; }
  .body-how { top: 671px; width: 522px; text-align: justify; }
  .body-last { top: 794px; width: 584px; text-align: justify; }
  .footer-rule { position: absolute; left: 224px; top: 910px; width: 745px; height: 2px; background: var(--rule); }
  .brand-name {
    position: absolute; left: 268px; top: 928px;
    font-family: "Roboto", Arial, sans-serif; font-weight: 700;
    font-size: 17px; line-height: 22px; color: var(--brand-ink);
  }
</style>
</head>
<body>
<main class="canvas">
  <svg class="page-art" width="1200" height="1000" viewBox="0 0 1200 1000">
    <defs>
      <linearGradient id="portraitTone" x1="0" y1="0" x2="1" y2="1">
        <stop offset="0" stop-color="#e9e4df"/>
        <stop offset="0.45" stop-color="#b98866"/>
        <stop offset="1" stop-color="#e9e4df"/>
      </linearGradient>
    </defs>
    <polygon class="portrait" role="img" aria-label="Portrait of a woman with curly hair touching her temples"
      points="705,15 969,15 969,755 448,333" fill="url(#portraitTone)"/>
    <polygon class="accent-chevron" points="930,15 969,15 969,100 812,295 969,420 969,535 690,320"
      fill="var(--accent-red)" opacity="0.88"/>
    <polygon class="headline-panel" points="224,15 705,15 448,333 490,372 381,502 224,377"
      fill="var(--brand-orange)"/>
  </svg>

  <h1 class="headline">Can<br>You<br>Make<br>Your<br>Neurelax<br>Last<br>Longer?</h1>

  <p class="article intro">Aging is a fact of life but looking your age isn't! "Keep calm and get Neurelax",<br>they say. But what if the recent lockdown has rendered both impossible? Is there a<br>way you can prolong the magical effects of expensive injections during the syringe<br>hiatus? We sought advice board-certified advice from professionals to bring you the answer.</p>

  <h2 class="section-heading heading-how">How Does Neurelax Work?</h2>
  <p class="article body-how">Neurelax reduces dynamic wrinkles but not ones caused by UV damage or gravity.Toxins from Clostridium botulinum is injected in minute amounts to block signals from nerves and cause paralysis. Neurelax only lasts for about 3 to 12 months depending on individuals.</p>

  <h2 class="section-heading heading-last">Is it Possible to Make Neurelax and Fillers Last Longer?</h2>
  <p class="article body-last">Neurelax is not permanent because new nerve endings grow to stimulate muscle movement again. NY Facial plastic surgeon, Dr. Aurelio Brannock says that many uncontrollable factors determine how long they last. Such include variability in an individual's metabolism and immune response. Both him and dermatologist, Dr. Selene Marwick, however, agree on some simple ways to prolong the results of Neurelax.</p>

  <div class="footer-rule"></div>
  <div class="brand-name">FernBloom Clinic</div>
</main>
</body>
</html>
```